Postcard Design for Vorn Imaging

I am a local photographer who specializes in real estate photography. High quality images with digital delivery within 24 hours.www.vorn-imaging.example marcusdelbrayimaging@mailbox.example

Industry/Entity Type

Real Estate

Requirements
Nice to have
• I've attached an image (emberpeak) with a watchtower. I love this STYLE of art. Emulating that style for the background, only using my colors (green, grey, white, black) would be pretty sweet!
Should not have
• I do not need space on backside for mailing.

```html
<!DOCTYPE html>
<html lang="en">
<head>
<meta charset="utf-8">
<title>Vorn Imaging – Real Estate Photography Postcard</title>
<link href="https://fonts.googleapis.com/css2?family=Arimo&family=Josefin+Sans:wght@300;400&display=swap" rel="stylesheet">
<style>
  :root {
    --page: #e9e9e7;
    --card: #ffffff;
    --header-grey: #a7a8aa;
    --brand-green: #1a9a60;
    --green-mid: #a6c8b5;
    --green-pale: #d4e3da;
    --wave-grey: #e6e7e8;
    --text-grey: #6d6e70;
    --photo-house: #8f9a78;
    --photo-deck: #9c8a63;
    --photo-bedroom: #a9b8bd;
  }
  * { margin: 0; padding: 0; box-sizing: border-box; }
  html, body { width: 1200px; height: 955px; overflow: hidden; background: var(--page); }
  .postcard {
    position: absolute; left: 20px; top: 27px;
    width: 1160px; height: 900px;
    background: var(--card);
    overflow: hidden;
  }
  .brand {
    position: absolute; left: 0; top: 0; width: 363px; height: 138px;
    display: flex; align-items: center; justify-content: center; gap: 14px;
  }
  .brand-dot { width: 40px; height: 40px; border-radius: 50%; background: var(--brand-green); }
  .brand-name {
    font-family: "Josefin Sans", sans-serif; font-weight: 300;
    font-size: 44px; color: var(--brand-green); line-height: 1; padding-top: 6px;
  }
  .booking-bar {
    position: absolute; left: 363px; top: 0; right: 0; height: 133px;
    background: var(--header-grey); color: #fff;
    font-family: "Arimo", sans-serif;
    padding: 42px 0 0 34px;
  }
  .booking-cta { font-size: 30px; letter-spacing: 0.2px; }
  .booking-contact { font-size: 21px; margin-top: 14px; }
  .booking-contact .divider { margin: 0 12px; }
  .photo { position: absolute; }
  .photo-house { left: 0; top: 141px; width: 747px; height: 489px;
    background: linear-gradient(180deg, #dfe3e6 0%, #b9b3a6 45%, var(--photo-house) 75%, #6f7f4a 100%); }
  .photo-deck { left: 756px; top: 141px; width: 404px; height: 240px;
    background: linear-gradient(180deg, #9fc0e4 0%, #6f9f4e 40%, var(--photo-deck) 70%, #8a5f3c 100%); }
  .photo-bedroom { left: 756px; top: 390px; width: 404px; height: 240px;
    background: linear-gradient(180deg, #d9e4e6 0%, var(--photo-bedroom) 50%, #5d4a3f 80%, #c9bfae 100%); }
  .headline {
    position: absolute; left: 0; right: 0; top: 662px; text-align: center;
    font-family: "Josefin Sans", sans-serif; font-weight: 300;
    font-size: 48px; letter-spacing: 1px; color: var(--text-grey);
  }
  .tagline {
    position: absolute; left: 0; right: 0; top: 727px; text-align: center;
    font-family: "Josefin Sans", sans-serif; font-weight: 400;
    font-size: 21px; color: var(--text-grey);
  }
  .wave-band { position: absolute; left: 0; bottom: 0; width: 1160px; height: 125px; }
</style>
</head>
<body>
  <main class="postcard">
    <div class="brand">
      <span class="brand-dot"></span>
      <span class="brand-name">Vorn Imaging</span>
    </div>
    <header class="booking-bar">
      <p class="booking-cta">BOOK A SHOOT NOW</p>
      <p class="booking-contact">www.vorn-imaging.example<span class="divider">|</span>marcusdelbrayimaging@mailbox.example</p>
    </header>

    <div class="photo photo-house" role="img" aria-label="Rear exterior of a two-storey house with a wooden gazebo, stone patio and bare trees"></div>
    <div class="photo photo-deck" role="img" aria-label="Wooden deck with patio table, chairs and umbrella overlooking green lawn"></div>
    <div class="photo photo-bedroom" role="img" aria-label="Bright bedroom with wooden bed, blue patterned quilt and bedside lamps"></div>

    <h1 class="headline">REAL ESTATE PHOTOGRAPHY</h1>
    <p class="tagline">High quality images with digital delivery within 24 hours</p>

    <svg class="wave-band" viewBox="0 0 1160 125" preserveAspectRatio="none" aria-hidden="true">
      <path d="M0 20 C250 -5 700 5 1160 12 L1160 125 L0 125 Z" fill="var(--wave-grey)"/>
      <path d="M0 38 C300 60 750 25 1160 38 L1160 125 L0 125 Z" fill="var(--green-pale)"/>
      <path d="M0 58 C350 78 800 42 1160 50 L1160 125 L0 125 Z" fill="var(--green-mid)"/>
      <path d="M0 88 C300 62 700 72 1160 66 L1160 125 L0 125 Z" fill="var(--brand-green)"/>
    </svg>
  </main>
</body>
</html>
```